To Build a Wordpress Website/Blog Post

I want to build a wordpress website and blog platform for a personal
Transformation project that will also form part of a multi channel/platform offering inc Instagram, podcasts, Facebook, YouTube all of which I am looking for help on. I will aim to blog c 1/2 times per week and would like to build an interactive offering that is future proof in terms
Of sizing and extension into another larger brand offering. (Can anyone pls tell me if/why I would Need a coded design? I’m afraid I don’t Know If I need this?). Tha is
Updates

Have now added ‘coded’ as an upgrade so worth allowing more time For designers

All. Just to let you know that I have added ‘coded’ as an upgrade as I want the Wordpress website to Be built as well as designed. Please see TomVale.com for the look and feel I want. I do not need the exommerce functionality at this time but if we could have each of those menu items built that would be great. The ones to show are Home, blog, podcast, Gavins Story, contact, resources plus maybe links to Instagram, Facebook and YouTube? Many tha ks

Target Market(s)

Men ages 35-60. Corporate, professional crowd for sure but all males globally. Ex athletes, Dads, interested in health and well-being. Endurance athletes. Interested in men’s health inc mental health, burnout, stress, middle age, life switching, potentiality, direction.

Industry/Entity Type

Health And Wellness

Coding

Coded - Design and coding required

Number of Pages Required

5+ page

Font styles to use
Serif
Sans Serif

Colors
3277b5
33a6d7
0493ce
acd136
1b1b1b
b1b1b1
b2b2b2
dddddd

Requirements
Must have
• A professional but inspirational appearance. Wordpress platform. Needs to host blogs and podcasts and images and feedback/forums plus archives and linking into a multi channel/platform offering. I need to
• Own the ip, be able to post text and images from mobile. It must be responsive and inc my logos and be editable by me at any time/registered in my Name. I enjoy greyscale and muted shades but will highlight other colours below
Nice to have
• See tomvale for high production values. This will Appeal to professionals (mostly men) that are aged 35-60 and interested in transformation. The idea is to do 50 things by the time I am 50 (Nov 19). So will update and blog etc but also Link to podcasts and Instagram and fbook etc
Should not have
• Too many cliches. Poor design and low production values. Needs to be aspirational

```html
<!DOCTYPE html>
<html lang="en">
<head>
<meta charset="utf-8">
<title>Personal Transformation – Home</title>
<link href="https://fonts.googleapis.com/css2?family=Roboto:wght@300;400;500;700;900&display=swap" rel="stylesheet">
<style>
:root{
  --page:#ffffff;
  --ink:#1b1b1b;
  --muted:#555555;
  --yellow:#f2c84b;
  --yellow-soft:#f9e7b0;
  --band-grey:#f2f2f2;
  --footer:#000000;
  --footer-text:#b1b1b1;
  --line:#dddddd;
  --play:#2ee07a;
  --tag-blue:#33a6d7;
  --tag-red:#e2504a;
  --tag-green:#3ed8a0;
}
*{box-sizing:border-box;margin:0;padding:0}
html,body{width:1200px;height:1200px;overflow:hidden;background:var(--page)}
body{position:relative;font-family:'Roboto',sans-serif;color:var(--ink)}
.abs{position:absolute}
.logo{left:428px;top:5px;font-size:14px;font-weight:300;letter-spacing:.5px}
.nav{left:534px;top:10px;display:flex;gap:10px;font-size:4px;font-weight:500;letter-spacing:.2px;align-items:center}
.social-top{left:731px;top:9px;display:flex;gap:3px}
.dot{display:block;border-radius:50%}
.social-top .dot{width:8px;height:8px}
.hero{left:406px;top:32px;width:388px;height:200px;
  background:linear-gradient(180deg,#3a6f8c 0%,#b99a66 35%,#e8b766 52%,#3f7690 70%,#1f4f6a 100%)}
.hero-title{left:600px;top:52px;color:#fff;font-size:13.5px;font-weight:700;line-height:16px}
.hero-copy{left:600px;top:88px;color:#fff;font-size:4px;line-height:5.6px;width:180px}
.btn{background:var(--yellow);color:var(--ink);font-size:3.6px;font-weight:700;letter-spacing:.3px;display:flex;align-items:center;justify-content:center}
.hero-btn{left:600px;top:107px;width:45px;height:11px}
.portrait{left:574px;top:194px;width:196px;height:187px;
  background:linear-gradient(120deg,#7a6a3c 0%,#3b3526 50%,#2b2f6e 85%,#4a4ad0 100%);box-shadow:0 4px 10px rgba(0,0,0,.3)}
.h2{font-size:11px;font-weight:700;letter-spacing:.1px}
.copy{font-size:3.6px;line-height:5.2px;color:var(--muted)}
.blog-h{left:433px;top:269px}
.blog-copy{left:433px;top:289px;width:122px}
.blog-btn{left:433px;top:329px;width:45px;height:11px}
.card{top:432px;height:90px;display:flex;align-items:flex-end;padding:0 0 9px 10px}
.card p{font-size:5.6px;line-height:6.6px;color:#333;position:relative}
.card-left{left:406px;width:120px;background:linear-gradient(180deg,#5f7a45 0%,#a8b890 55%,#fff 100%)}
.card-mid{left:526px;top:425px;width:148px;height:104px;padding:0 0 9px 18px;
  background:linear-gradient(180deg,#5d6c7a 0%,#d9a86a 35%,#9a8f6a 60%,#fff 100%);box-shadow:0 4px 10px rgba(0,0,0,.3)}
.card-right{left:674px;width:120px;background:linear-gradient(180deg,#9b9b95 0%,#d8d8d2 55%,#fff 100%)}
.video{left:406px;top:570px;width:223px;height:150px;
  background:radial-gradient(circle at 30% 60%,#e3a3c2 0%,#9a5e8a 35%,#3a3550 75%,#262a3c 100%)}
.play{left:498px;top:625px;width:40px;height:40px}
.pod-h{left:646px;top:606px}
.pod-copy{left:646px;top:624px;width:122px}
.pod-btn{left:646px;top:664px;width:45px;height:11px}
.subscribe{left:406px;top:753px;width:388px;height:134px;background:var(--yellow)}
.sub-h{left:406px;top:774px;width:388px;text-align:center;font-size:11px;font-weight:700}
.sub-copy{left:460px;top:794px;width:280px;text-align:center;font-size:3.4px;line-height:5px;color:#333}
.sub-form{left:513px;top:817px;width:159px;height:12px;display:flex}
.sub-input{flex:1;background:var(--yellow-soft);font-size:4px;color:#777;padding-left:5px;display:flex;align-items:center}
.sub-btn{width:46px;background:#fff;font-size:3.6px;font-weight:700;display:flex;align-items:center;justify-content:center}
.couple{left:596px;top:849px;width:174px;height:181px;
  background:linear-gradient(180deg,#e9d9c2 0%,#cdb597 45%,#a98a63 70%,#7c6546 100%)}
.tag-featured{left:446px;top:921px;background:var(--yellow);font-size:3.6px;padding:1px 2px}
.feat-h{left:446px;top:933px;font-size:8.5px;font-weight:700}
.feat-copy{left:446px;top:950px;width:122px}
.feat-btn{left:446px;top:991px;width:45px;height:11px}
.follow{left:406px;top:1054px;width:388px;height:34px;background:var(--band-grey);display:flex;align-items:center;justify-content:center;gap:10px}
.follow h3{font-size:11px;font-weight:700;margin-left:-20px}
.follow-icons{display:flex;gap:5px}
.follow-icons .dot{width:16px;height:16px}
.footer{left:406px;top:1089px;width:388px;height:89px;background:var(--footer);color:var(--footer-text)}
.fcol{position:absolute;top:13px}
.fcol h4{font-size:5px;font-weight:700;color:#fff;padding-bottom:5px;border-bottom:1px solid #555;margin-bottom:8px}
.fcol ul{list-style:none;font-size:3.4px;line-height:5.4px}
.contact li{display:flex;gap:4px;margin-bottom:4px}
.ico{width:5px;height:5px;flex:none}
.tags{display:flex;flex-wrap:wrap;gap:3px;width:72px}
.tag{font-size:3.4px;padding:1px 2px;color:#111}
.copyright{left:406px;top:1184px;width:388px;text-align:center;font-size:3.6px;letter-spacing:.8px;color:#333}
</style>
</head>
<body>

<header>
  <div class="abs logo">LOGO</div>
  <nav class="abs nav">
    <span>HOME</span><span>BLOG</span><span>PODCAST</span><span>GAVINS STORY</span><span>CONTACT</span>
    <svg width="6" height="6" viewBox="0 0 10 10"><circle cx="4" cy="4" r="3" fill="none" stroke="#1b1b1b" stroke-width="1.2"/><line x1="6.2" y1="6.2" x2="9" y2="9" stroke="#1b1b1b" stroke-width="1.2"/></svg>
  </nav>
  <div class="abs social-top">
    <span class="dot" style="background:#3b5998" aria-label="Social link"></span>
    <span class="dot" style="background:#1da1f2" aria-label="Social link"></span>
    <span class="dot" style="background:#0077b5" aria-label="Social link"></span>
    <span class="dot" style="background:#dd4b39" aria-label="Social link"></span>
  </div>
</header>

<section class="hero-section">
  <div class="abs hero" role="img" aria-label="Photo of a man on a cliff edge with arms raised above the sea at sunset"></div>
  <h1 class="abs hero-title">PERSONAL<br>TRANSFORMATION</h1>
  <p class="abs hero-copy">Uniquely utilize end-to-end growth strategies whereas distinctive technologies. Dramatically predominate one-to-one imperatives</p>
  <div class="abs btn hero-btn">LEARN MORE</div>
  <div class="abs portrait" role="img" aria-label="Photo of a speaker in a suit gesturing on stage"></div>
</section>

<section class="blog">
  <h2 class="abs h2 blog-h">LATEST BLOG POST</h2>
  <p class="abs copy blog-copy">Uniquely utilize end-to-end growth strategies whereas distinctive technologies. Dramatically predominate one-to-one imperatives without top-line internal or "organic" sources. Professionally network ethical expertise rather than equity invested value. Phosfluorescently re-engineer timely vortals for B2B vortals. Phosfluorescently exploit empowered users vis-a-vis open-source synergy.</p>
  <div class="abs btn blog-btn">READ MORE</div>
</section>

<section class="cards">
  <div class="abs card card-left" role="img" aria-label="Photo of a child leaping joyfully outdoors"><p>Interactively grow leading-edge<br>interfaces through</p></div>
  <div class="abs card card-right" role="img" aria-label="Photo of a man in a bright modern office"><p>Interactively grow leading-edge<br>interfaces through</p></div>
  <div class="abs card card-mid" role="img" aria-label="Photo of a person with open arms in a field at sunrise"><p>Interactively grow leading-edge<br>interfaces through</p></div>
</section>

<section class="podcasts">
  <div class="abs video" role="img" aria-label="Photo of a concert crowd with raised fists in coloured smoke"></div>
  <svg class="abs play" viewBox="0 0 40 40" aria-label="Play">
    <circle cx="20" cy="20" r="20" fill="var(--play)"/>
    <circle cx="20" cy="20" r="11" fill="none" stroke="#fff" stroke-width="2"/>
    <path d="M17 14.5 L25.5 20 L17 25.5 Z" fill="#fff"/>
  </svg>
  <h2 class="abs h2 pod-h">RECENT PODCASTS</h2>
  <p class="abs copy pod-copy">Uniquely utilize end-to-end growth strategies whereas distinctive technologies. Dramatically predominate one-to-one imperatives without top-line internal or "organic" sources. Professionally network ethical expertise rather than equity invested value. Phosfluorescently re-engineer timely vortals for B2B vortals. Phosfluorescently exploit empowered users vis-a-vis open-source synergy.</p>
  <div class="abs btn pod-btn">READ MORE</div>
</section>

<section class="newsletter">
  <div class="abs subscribe"></div>
  <h2 class="abs sub-h">SUBSCRIBE TO BE THE FIRST TO KNOW</h2>
  <p class="abs sub-copy">Uniquely utilize end-to-end growth strategies whereas distinctive technologies. Dramatically predominate one-to-one imperatives without top-line internal or "organic" sources. Professionally network ethical expertise rather than equity invested value. Phosfluorescently</p>
  <div class="abs sub-form"><div class="sub-input">Email</div><div class="sub-btn">SUBSCRIBE</div></div>
  <div class="abs couple" role="img" aria-label="Photo of a couple embracing in a field at golden hour"></div>
  <span class="abs tag-featured">FEATURED</span>
  <h3 class="abs feat-h">YOUR HEADING</h3>
  <p class="abs copy feat-copy">Uniquely utilize end-to-end growth strategies whereas distinctive technologies. Dramatically predominate one-to-one imperatives without top-line internal or "organic" sources. Professionally network ethical expertise rather than equity invested value. Phosfluorescently re-engineer timely vortals for B2B vortals. Phosfluorescently exploit empowered users vis-a-vis open-source synergy.</p>
  <div class="abs btn feat-btn">READ MORE</div>
</section>

<section class="abs follow">
  <h3>FOLLOW US ON</h3>
  <div class="follow-icons">
    <span class="dot" style="background:#1ab7a0" aria-label="Social link"></span>
    <span class="dot" style="background:#2ca5e0" aria-label="Social link"></span>
    <span class="dot" style="background:#3b5998" aria-label="Social link"></span>
    <span class="dot" style="background:#55acee" aria-label="Social link"></span>
    <span class="dot" style="background:#0077b5" aria-label="Social link"></span>
    <span class="dot" style="background:#dd4b39" aria-label="Social link"></span>
  </div>
</section>

<footer class="abs footer">
  <div class="fcol contact" style="left:22px;width:60px">
    <h4>CONTACT INFO</h4>
    <ul>
      <li><svg class="ico" viewBox="0 0 10 10"><path d="M2 1 L4 1 L5 3 L4 4 Q5 6 6 6 L7 5 L9 6 L9 8 Q5 9 1 3 Z" fill="none" stroke="#b1b1b1" stroke-width=".8"/></svg>0123232425435</li>
      <li><svg class="ico" viewBox="0 0 10 10"><path d="M1 5 L5 1.5 L9 5 M2.5 4 V9 H7.5 V4" fill="none" stroke="#b1b1b1" stroke-width=".8"/></svg><span>Dramatically enhance<br>excellent e business<br>1212 abc</span></li>
      <li><svg class="ico" viewBox="0 0 10 10"><rect x="1" y="2.5" width="8" height="5.5" fill="none" stroke="#b1b1b1" stroke-width=".8"/><path d="M1 2.5 L5 6 L9 2.5" fill="none" stroke="#b1b1b1" stroke-width=".8"/></svg>info@email.com</li>
    </ul>
  </div>
  <div class="fcol" style="left:102px;width:62px">
    <h4>SITE NAVIGATIUON</h4>
    <ul><li>Home</li><li>Blog</li><li>Podcast</li><li>Gavins story</li><li>Contact</li><li>Signin</li><li>Newsletter</li></ul>
  </div>
  <div class="fcol" style="left:192px;width:62px">
    <h4>USEFUL LINKS</h4>
    <ul><li>Tearms &amp; condition</li><li>Site Map</li><li>Social Links</li><li>follow us</li><li>Privacy policy</li></ul>
  </div>
  <div class="fcol" style="left:280px;width:62px">
    <h4>TAGS</h4>
    <div class="tags">
      <span class="tag" style="background:var(--tag-blue)">TECH</span>
      <span class="tag" style="background:var(--yellow)">FEATURED</span>
      <span class="tag" style="background:var(--tag-red)">TRANDING</span>
      <span class="tag" style="background:var(--tag-green)">NATUTRE</span>
      <span class="tag" style="background:var(--tag-blue)">TECH</span>
      <span class="tag" style="background:var(--yellow)">FEATURED</span>
      <span class="tag" style="background:var(--tag-red)">TRANDING</span>
      <span class="tag" style="background:var(--tag-green)">NATUTRE</span>
    </div>
  </div>
</footer>

<p class="abs copyright">© GAVIN.COM IS THE PROPERTY OF GAVIN 2004-2016. ALL RIGHTS RESERVED.</p>

</body>
</html>
```